'Tarvel' a financial/crypto-currency exchange in the middle east

On the card we need 1) Name 2) title 3) email address 4) phone number using the same colors and theme as the logo. On one side we just want the logo and we want the whole card to be in blue (same blue as logo) with the logo in the back being white.
Industry/Entity Type
Financial

```html
<!DOCTYPE html>
<html lang="en">
<head>
<meta charset="UTF-8">
<title>Tarvel Business Card</title>
<link href="https://fonts.googleapis.com/css2?family=Poppins:wght@600&family=Open+Sans:wght@400;500&display=swap" rel="stylesheet">
<style>
  :root {
    --brand-blue: #0b91cc;
    --band-blue: #6badde;
    --white: #ffffff;
    --backdrop: #dcdbd9;
  }
  * { margin: 0; padding: 0; box-sizing: border-box; }
  html, body {
    width: 1200px;
    height: 1000px;
    overflow: hidden;
    background: var(--backdrop);
  }
  .canvas {
    position: relative;
    width: 1200px;
    height: 1000px;
  }
  .card {
    position: absolute;
    background: var(--brand-blue);
    border-radius: 40px;
    overflow: hidden;
  }
  .card-front { left: 150px; top: 103px; width: 630px; height: 360px; }
  .card-back  { left: 370px; top: 545px; width: 638px; height: 363px; }

  .corner-frame { position: absolute; inset: 0; }

  .brand {
    position: absolute;
    display: flex;
    align-items: center;
    color: var(--white);
    font-family: "Poppins", sans-serif;
    font-weight: 600;
  }
  .brand-mark {
    border-radius: 50%;
    background: var(--white);
    flex: none;
  }
  .card-front .brand { left: 142px; top: 138px; gap: 30px; font-size: 58px; letter-spacing: 0.5px; }
  .card-front .brand-mark { width: 96px; height: 96px; }
  .card-back .brand { left: 214px; top: 47px; gap: 14px; font-size: 33px; }
  .card-back .brand-mark { width: 60px; height: 60px; }

  .name-ribbon { position: absolute; left: 0; top: 130px; width: 638px; height: 90px; }
  .person-name {
    position: absolute;
    left: 0; width: 638px; top: 137px;
    text-align: center;
    font-family: "Open Sans", sans-serif;
    font-weight: 500;
    font-size: 28px;
    letter-spacing: 1.5px;
    color: var(--brand-blue);
  }
  .person-title {
    position: absolute;
    left: 0; width: 638px; top: 184px;
    text-align: center;
    font-family: "Open Sans", sans-serif;
    font-size: 18px;
    letter-spacing: 1.5px;
    color: var(--white);
  }
  .contact-list {
    position: absolute;
    left: 184px; top: 244px;
    list-style: none;
    color: var(--white);
    font-family: "Open Sans", sans-serif;
    font-size: 23px;
    letter-spacing: 1.5px;
  }
  .contact-item { display: flex; align-items: center; gap: 18px; height: 40px; }
  .contact-icon { width: 26px; height: 26px; flex: none; }
</style>
</head>
<body>
<main class="canvas">

  <section class="card card-front" aria-label="Card front">
    <svg class="corner-frame" width="630" height="360" viewBox="0 0 630 360" fill="none" stroke="#ffffff" stroke-width="2">
      <path d="M110 38 H58 A22 22 0 0 0 36 60 V112"/>
      <path d="M520 38 H572 A22 22 0 0 1 594 60 V112"/>
      <path d="M36 250 V302 A22 22 0 0 0 58 324 H110"/>
      <path d="M594 250 V302 A22 22 0 0 1 572 324 H520"/>
    </svg>
    <div class="brand">
      <span class="brand-mark"></span>
      <span class="brand-name">Tarvel</span>
    </div>
  </section>

  <section class="card card-back" aria-label="Card back">
    <div class="brand">
      <span class="brand-mark"></span>
      <span class="brand-name">Tarvel</span>
    </div>

    <svg class="name-ribbon" width="638" height="90" viewBox="0 0 638 90">
      <path d="M82 49 H548 V62 A22 22 0 0 1 526 83 H104 A22 22 0 0 1 82 62 Z" fill="#6badde"/>
      <path d="M35 49 L55 16 Q62 7 80 7 H568 Q578 7 584 16 L602 49 Z" fill="#ffffff"/>
    </svg>
    <p class="person-name">Name of Person</p>
    <p class="person-title">Title of person</p>

    <ul class="contact-list">
      <li class="contact-item">
        <svg class="contact-icon" viewBox="0 0 26 26" fill="none" stroke="#ffffff" stroke-width="2">
          <circle cx="13" cy="13" r="11.5"/>
          <path d="M9 7.5 L11 10.5 L9.8 12 Q11 15 14 16.2 L15.5 15 L18.5 17 L17 19 Q12 19 9 15.5 Q6.8 12 7.5 8.5 Z" fill="#ffffff" stroke="none"/>
        </svg>
        <span>Phone number</span>
      </li>
      <li class="contact-item">
        <svg class="contact-icon" viewBox="0 0 26 26">
          <circle cx="13" cy="13" r="12.5" fill="#ffffff"/>
          <rect x="6.5" y="8.5" width="13" height="9" rx="1" fill="#0b91cc"/>
          <path d="M6.8 9 L13 13.8 L19.2 9" fill="none" stroke="#ffffff" stroke-width="1.4"/>
        </svg>
        <span>name@email.com</span>
      </li>
    </ul>
  </section>

</main>
</body>
</html>
```